Business Cards

We were billed for this because the project timed out. Please give me another designed to open this back up. I was not happy with the last designs (that I was charged for).
we are also using the logo with Clear Water Care Done Right Every Time
Also want to utilize Where Healthy Water is our Commitment.

Contact Information for Business Card

Marlowe Stone Group Inc

```html
<!DOCTYPE html>
<html lang="en">
<head>
<meta charset="utf-8">
<title>Marlowe Stone Group – Business Cards</title>
<link rel="stylesheet" href="https://fonts.googleapis.com/css2?family=Montserrat:wght@500;600;800&family=Questrial&display=swap">
<style>
  :root {
    --stage: #e6e7e9;
    --card-white: #ffffff;
    --card-dark: #101112;
    --brand-blue: #2f7fc4;
    --brand-blue-deep: #1b5e9c;
    --ink: #1c1d1f;
    --ink-soft: #4a4d52;
    --dark-name: #6d7074;
    --dark-tag: #50535a;
    --light-text: #f2f3f4;
  }
  * { box-sizing: border-box; margin: 0; padding: 0; }
  html, body { width: 1200px; height: 900px; overflow: hidden; }
  body {
    background: var(--stage);
    position: relative;
    font-family: "Questrial", "Century Gothic", sans-serif;
  }
  .card {
    position: absolute;
    width: 620px;
    height: 354px;
    box-shadow: 0 10px 28px rgba(0,0,0,.18);
  }

  /* Front */
  .card--front {
    left: 140px; top: 70px;
    background: var(--card-white);
    border-radius: 34px 0 34px 0;
  }
  .front-web {
    position: absolute;
    top: 36px; right: 36px;
    font-family: "Montserrat", sans-serif;
    font-weight: 600;
    font-size: 15px;
    letter-spacing: 4px;
    color: var(--ink);
    white-space: nowrap;
  }
  .front-web .domain { color: var(--brand-blue-deep); }
  .wordmark {
    position: absolute;
    display: flex;
    align-items: center;
    gap: 14px;
    white-space: nowrap;
  }
  .wordmark__square {
    width: 34px; height: 34px;
    background: var(--brand-blue);
    flex: none;
  }
  .wordmark__name {
    font-family: "Montserrat", sans-serif;
    font-weight: 800;
    font-size: 25px;
    letter-spacing: 1px;
    line-height: 1;
    color: var(--ink);
  }
  .wordmark__tag {
    font-family: "Questrial", sans-serif;
    font-size: 11px;
    letter-spacing: 2.6px;
    margin-top: 6px;
    color: var(--ink-soft);
  }
  .card--front .wordmark { left: 90px; bottom: 78px; }

  /* Back */
  .card--back {
    left: 440px; top: 476px;
    background: var(--card-dark);
    border-radius: 0 34px 0 34px;
    color: var(--light-text);
  }
  .holder {
    position: absolute;
    left: 40px; top: 40px;
  }
  .holder__name {
    font-family: "Montserrat", sans-serif;
    font-weight: 600;
    font-size: 22px;
    color: var(--brand-blue);
    letter-spacing: .5px;
  }
  .holder__role {
    font-size: 17px;
    margin-top: 4px;
  }
  .contacts {
    position: absolute;
    right: 40px; top: 42px;
    width: 300px;
    list-style: none;
  }
  .contacts li {
    display: flex;
    align-items: center;
    gap: 10px;
    font-size: 15.5px;
    line-height: 1;
    padding: 5px 0;
    white-space: nowrap;
  }
  .contacts svg { width: 16px; height: 16px; flex: none; fill: var(--brand-blue); }
  .divider {
    position: absolute;
    right: 40px; top: 196px;
    width: 300px;
    height: 1px;
    background: var(--brand-blue-deep);
  }
  .card--back .wordmark { right: 40px; top: 222px; }
  .card--back .wordmark__name { color: var(--dark-name); font-size: 21px; }
  .card--back .wordmark__tag { color: var(--dark-tag); font-size: 9.5px; letter-spacing: 2.2px; }
  .card--back .wordmark__square { width: 30px; height: 30px; }
</style>
</head>
<body>

<section class="card card--front" aria-label="Business card front">
  <p class="front-web">www.<span class="domain">marlowestonegroup</span>.com</p>
  <div class="wordmark">
    <span class="wordmark__square"></span>
    <div>
      <p class="wordmark__name">MARLOWE STONE GROUP</p>
      <p class="wordmark__tag">CLEAR WATER CARE DONE RIGHT EVERY TIME</p>
    </div>
  </div>
</section>

<section class="card card--back" aria-label="Business card back">
  <div class="holder">
    <p class="holder__name">JOHN SMITH</p>
    <p class="holder__role">Director</p>
  </div>

  <ul class="contacts">
    <li>
      <svg viewBox="0 0 24 24" aria-hidden="true"><path d="M6.6 10.8a15.1 15.1 0 0 0 6.6 6.6l2.2-2.2c.3-.3.7-.4 1-.2 1.1.4 2.3.6 3.6.6.6 0 1 .4 1 1V20c0 .6-.4 1-1 1C10.6 21 3 13.4 3 4c0-.6.4-1 1-1h3.5c.6 0 1 .4 1 1 0 1.3.2 2.5.6 3.6.1.3 0 .7-.2 1z"/></svg>
      555-014-7261
    </li>
    <li>
      <svg viewBox="0 0 24 24" aria-hidden="true"><path d="M2 5h20v14H2zm2 2v.5l8 5 8-5V7zm0 2.8V17h16V9.8l-8 5z"/></svg>
      john@marlowestonegroup.com
    </li>
    <li>
      <svg viewBox="0 0 24 24" aria-hidden="true"><path d="M12 2a10 10 0 1 0 0 20 10 10 0 0 0 0-20zm6.9 6h-3a15 15 0 0 0-1.3-3.9A8 8 0 0 1 18.9 8zM12 4c.8 1.2 1.5 2.5 1.9 4h-3.8c.4-1.5 1.1-2.8 1.9-4zM4.3 14a8 8 0 0 1 0-4h3.4a16 16 0 0 0 0 4zm.8 2h3a15 15 0 0 0 1.3 3.9A8 8 0 0 1 5.1 16zm3-8h-3a8 8 0 0 1 4.3-3.9C8.8 5.3 8.4 6.6 8.1 8zM12 20c-.8-1.2-1.5-2.5-1.9-4h3.8c-.4 1.5-1.1 2.8-1.9 4zm2.3-6H9.7a14 14 0 0 1 0-4h4.6a14 14 0 0 1 0 4zm.3 5.9c.6-1.200 1-2.5 1.3-3.900h3a8 8 0 0 1-4.3 3.9zm1.7-5.9a16 16 0 0 0 0-4h3.4a8 8 0 0 1 0 4z"/></svg>
      www.marlowestonegroup.com
    </li>
    <li>
      <svg viewBox="0 0 24 24" aria-hidden="true"><path d="M12 2a7 7 0 0 0-7 7c0 5.2 7 13 7 13s7-7.8 7-13a7 7 0 0 0-7-7zm0 9.5a2.5 2.5 0 1 1 0-5 2.5 2.5 0 0 1 0 5z"/></svg>
      00 dummy city, dummy place 0000
    </li>
  </ul>

  <div class="divider"></div>

  <div class="wordmark">
    <span class="wordmark__square"></span>
    <div>
      <p class="wordmark__name">MARLOWE STONE GROUP</p>
      <p class="wordmark__tag">CLEAR WATER CARE DONE RIGHT EVERY TIME</p>
    </div>
  </div>
</section>

</body>
</html>
```